Crowdsourced Research Platform: KOVAL Polls

KOVAL Polls is an acronym for Kindred Opinion Views Among Lands (KOVAL) Polls. This is a research effort to format and combine multiple sources of public opinion data from around the world into merged datasets. The website will at first mainly act as a quality control hub and distribution point for official dataset releases. It will provide resources such as codebooks, development guidelines, and instructional videos for crowdsourcing continued expansion of the resource. We need a coded (HTML and CSS) website design and associated files to launch the website with ease. We purchased the domain www.kovalpolls.org, but access is blocked while it is under construction.

The website design should be based on a logo recently commissioned (see attached). The design should be simple and professional with lots of white space. We would like the logo on the top left of all pages and the primary navigation menu along the top-right of all pages. The primary navigation menu should have a simple mouse-over effect and the main menu items should expand with secondary drop-down options. The footer should include a few columns with headings and links to different pages. The website layout should be dynamic and expand its width to fit different sized screens. There will be a lot of data and information displayed in tables, so we would like the CSS coding and website design to include tables designed to match the website theme. The main graphical content will be data visualisations such as pie/bar charts, histograms, scatter plots, heat maps, moving average trend lines etc. We would therefore like the design to include modular sections (boxes matching theme to display plots/graphs/etc) that can visually display these types of figures with text/caption underneath to explain the data visualizations.

For more information and written placeholder content, designers should read the attached documents to get a better idea about the project. Some draft working papers using merged datsets have been included for reference and you can use these for their examples of data visualizations and use the written content for filling in page content.

Target Market(s)

The primary target audience will be academics in universities and research institutes. The resource will be most useful to quantitative social scientists, particularly political scientists and sociologists, but any discipline concerned with us humans could find the resource useful. Others such as graduate-level university students, civil servants in government departments, members of research institutions, and policy researchers in non-profit organizations will also find the resource useful.

Coding

Coded - Design and coding required

Number of Pages Required

3 page

Font styles to use
Sans Serif

Colors

Designer to choose colors to be used in the design.

Requirements
Must have
• HTML and CSS coding (not Wordpress)
Nice to have
• Content boxes to display data visualizations alongside articles.

```html
<!DOCTYPE html>
<html lang="en">
<head>
<meta charset="utf-8">
<title>KOVAL Polls – Charts and Table</title>
<link rel="stylesheet" href="https://fonts.googleapis.com/css2?family=Roboto:wght@300;400;500&display=swap">
<style>
:root{
  --blue:#2f7fc1;
  --sky:#29a3dc;
  --grey:#9a9a9a;
  --ink:#333;
  --text:#555;
  --rule:#d9d9d9;
  --pale:#f4f5f6;
  --foot:#eef0f2;
}
*{box-sizing:border-box;margin:0;padding:0}
html,body{width:1069px;height:1200px;overflow:hidden;background:#fff}
body{font-family:'Roboto',sans-serif;color:var(--text);position:relative}
.board{position:relative;width:1069px;height:1200px}
.abs{position:absolute}

/* ---------- presentation sheet ---------- */
.sheet-title{left:101px;top:32px;font-size:41px;font-weight:300;letter-spacing:2.5px;color:var(--ink);border-bottom:2px solid var(--ink);line-height:44px;padding-bottom:0}
.data-table{left:98px;top:110px;width:550px;border-collapse:collapse;border:1px solid var(--rule);font-size:10px}
.data-table th{background:var(--pale);color:var(--blue);font-weight:400;font-size:11px;height:24px;border-bottom:1px solid var(--rule)}
.data-table td{height:23.8px;border-bottom:1px solid var(--rule);text-align:center;color:var(--text)}
.data-table td:first-child{text-align:left;padding-left:35px;border-right:1px solid var(--rule)}
.data-table td:nth-child(2){border-right:1px solid var(--rule)}
.data-table .col-src{width:272px}.data-table .col-yr{width:147px}
.chart-hist{left:72px;top:402px;width:579px;height:213px}
.legend{display:flex;gap:14px;font-size:10px;color:var(--text);align-items:center}
.legend span{display:flex;align-items:center;gap:6px}
.legend i{width:6px;height:6px;border-radius:50%;display:block}
.legend .male i{background:var(--blue)}.legend .female i{background:var(--grey)}
.legend-main{left:128px;top:659px}
.chart-scatter-l{left:76px;top:683px;width:261px;height:197px}
.chart-scatter-r{left:418px;top:683px;width:237px;height:197px}
.chart-title{font-size:12px;color:var(--blue);letter-spacing:.3px;text-align:center;width:160px}
.title-l{left:133px;top:912px}.title-r{left:454px;top:912px}
.chart-trade-l{left:84px;top:941px;width:253px;height:205px}
.chart-trade-r{left:405px;top:941px;width:253px;height:205px}
svg text{font-family:'Roboto',sans-serif}

/* ---------- website mock ---------- */
.site{left:707px;top:8px;width:312px;height:1189px;background:#fff;box-shadow:0 0 0 1px #e3e3e3;overflow:hidden;font-size:3.6px;line-height:5.2px}
.site > *{position:absolute}
.topbar{left:0;top:0;width:100%;height:12px;background:var(--sky);color:#fff;display:flex;justify-content:space-between;align-items:center;padding:0 16px 0 18px;font-size:3.4px}
.topbar nav{display:flex;gap:7px}
.masthead{left:0;top:12px;width:100%;height:24px;display:flex;align-items:center;justify-content:space-between;padding:0 10px 0 16px}
.brand{display:flex;align-items:center;gap:3px;color:var(--blue);font-size:7px;font-weight:500;line-height:1}
.brand i{width:6px;height:6px;border-radius:50%;background:var(--sky);display:block}
.mainnav{display:flex;gap:7px;font-size:3.3px;line-height:3.8px;color:#666}
.hero{left:0;top:24px;width:100%;height:87px;background:linear-gradient(180deg,#f7f8f9 0%,#e9ecee 55%,#d9dde0 100%)}
.hero-copy{left:34px;top:49px;width:160px}
.hero-copy .kicker{color:var(--sky);font-size:3.6px}
.hero-copy h2{color:var(--blue);font-size:5px;font-weight:400;line-height:6px;margin-bottom:2px}
.hero-copy p{color:#555}
.hero-copy .btn{display:inline-block;margin-top:4px;border:0.6px solid var(--sky);color:var(--sky);padding:1.5px 6px;font-size:3.2px;line-height:4px}
.toc{left:34px;top:127px;width:240px}
.toc h3{font-size:4.6px;font-weight:400;color:#444;margin-bottom:3px}
.toc h3 b{color:var(--sky);font-weight:400}
.toc-cols{display:flex;gap:22px;color:var(--blue);font-size:3.3px;line-height:6.8px}
.divider{left:0;top:185px;width:100%;height:0;border-top:0.6px solid #e6e6e6}
.sec-h{font-size:4.4px;color:#444;left:36px}
.copy{left:42px;width:236px;color:#777;font-size:3.4px;line-height:5.4px}
.step{left:36px;display:flex;align-items:center;gap:4px;color:var(--blue);font-size:3.4px}
.step i{width:6px;height:6px;background:var(--blue);display:block;border-radius:0.8px}
.mini-table{left:42px;top:450px;width:227px;border-collapse:collapse;border:0.6px solid #e2e2e2;font-size:3px;line-height:3px}
.mini-table th{background:var(--pale);color:var(--blue);font-weight:400;height:9px}
.mini-table td{height:10px;border-top:0.5px solid #e2e2e2;color:#777;text-align:center}
.mini-table td:first-child{text-align:left;padding-left:14px}
.mini-hist{left:39px;top:627px;width:230px;height:85px}
.mini-legend{left:44px;top:797px;font-size:3.2px;gap:5px}
.mini-legend i{width:2.4px;height:2.4px}
.mini-legend span{gap:2px}
.mini-scatter-l{left:37px;top:804px;width:109px;height:84px}
.mini-scatter-r{left:181px;top:804px;width:96px;height:84px}
.mini-ct{font-size:3.4px;color:var(--blue);width:80px;text-align:center}
.mini-trade-l{left:48px;top:986px;width:97px;height:83px}
.mini-trade-r{left:175px;top:986px;width:97px;height:83px}
.footer{left:0;top:1089px;width:100%;height:86px;background:var(--foot)}
.foot-brand{left:30px;top:1110px;width:74px}
.foot-brand .brand{font-size:6px}
.foot-brand p{color:#999;font-size:3px;line-height:4px;margin-top:4px}
.social{display:flex;gap:3px;margin-top:6px}
.social i{width:6px;height:6px;border-radius:50%;border:0.5px solid #bbb;display:block}
.foot-col{top:1108px;font-size:3.2px;line-height:7.2px;color:#444}
.foot-col h4{font-weight:400;color:#999;font-size:3.4px;margin-bottom:1px}
.bottombar{left:0;top:1175px;width:100%;height:14px;background:var(--sky);color:#e9f6fc;font-size:3px;display:flex;align-items:center;padding-left:16px}
</style>
</head>
<body>
<svg width="0" height="0" style="position:absolute" aria-hidden="true">
  <defs>
    <symbol id="hist" viewBox="90 500 720 265">
      <g stroke="#d5d5d5" stroke-dasharray="4 4" stroke-width="1">
        <line x1="120" y1="512" x2="806" y2="512"/><line x1="120" y1="586" x2="806" y2="586"/><line x1="120" y1="659" x2="806" y2="659"/>
      </g>
      <line x1="120" y1="503" x2="120" y2="733" stroke="#999"/>
      <line x1="120" y1="733" x2="806" y2="733" stroke="#999"/>
      <g fill="#2f7fc1">
        <rect x="146" y="729" width="13" height="4"/><rect x="170" y="726" width="13" height="7"/><rect x="195" y="718" width="13" height="15"/><rect x="220" y="715" width="13" height="18"/><rect x="244" y="723" width="13" height="10"/><rect x="269" y="712" width="13" height="21"/><rect x="293" y="692" width="13" height="41"/><rect x="318" y="663" width="13" height="70"/><rect x="342" y="652" width="13" height="81"/><rect x="367" y="619" width="13" height="114"/><rect x="391" y="600" width="13" height="133"/><rect x="415" y="575" width="13" height="158"/><rect x="440" y="531" width="13" height="202"/><rect x="465" y="531" width="13" height="202"/><rect x="489" y="612" width="13" height="121"/><rect x="513" y="597" width="13" height="136"/><rect x="538" y="572" width="13" height="161"/><rect x="563" y="612" width="13" height="121"/><rect x="587" y="612" width="13" height="121"/><rect x="612" y="610" width="13" height="123"/><rect x="636" y="576" width="13" height="157"/><rect x="660" y="555" width="13" height="178"/><rect x="685" y="565" width="13" height="168"/><rect x="709" y="642" width="13" height="91"/><rect x="734" y="651" width="13" height="82"/><rect x="758" y="712" width="13" height="21"/>
      </g>
      <path d="M140 730 C 290 705 390 560 505 557 C 600 554 690 620 772 708" fill="none" stroke="#c4c4c4" stroke-width="2.5"/>
      <g font-size="12" fill="#444" text-anchor="middle">
        <text transform="translate(107 512) rotate(-90)">60</text><text transform="translate(107 586) rotate(-90)">40</text><text transform="translate(107 659) rotate(-90)">20</text><text transform="translate(107 733) rotate(-90)">0</text>
        <text x="130" y="755">0</text><text x="197" y="755">10</text><text x="263" y="755">20</text><text x="330" y="755">30</text><text x="397" y="755">40</text><text x="463" y="755">50</text><text x="530" y="755">60</text><text x="597" y="755">70</text><text x="663" y="755">80</text><text x="730" y="755">90</text><text x="797" y="755">0</text>
      </g>
    </symbol>

    <symbol id="scatter" viewBox="125 850 295 245">
      <g stroke="#d8d8d8" stroke-dasharray="4 4">
        <line x1="150" y1="860" x2="418" y2="860"/><line x1="150" y1="913" x2="418" y2="913"/><line x1="150" y1="965" x2="418" y2="965"/><line x1="150" y1="1016" x2="418" y2="1016"/>
        <line x1="160" y1="856" x2="160" y2="1070"/><line x1="199" y1="856" x2="199" y2="1070"/><line x1="237" y1="856" x2="237" y2="1070"/><line x1="276" y1="856" x2="276" y2="1070"/><line x1="314" y1="856" x2="314" y2="1070"/><line x1="353" y1="856" x2="353" y2="1070"/><line x1="392" y1="856" x2="392" y2="1070"/>
      </g>
      <line x1="150" y1="856" x2="150" y2="1070" stroke="#999"/>
      <line x1="150" y1="1070" x2="418" y2="1070" stroke="#999"/>
      <g fill="#9a9a9a">
        <circle cx="172" cy="1045" r="2"/><circle cx="175" cy="1020" r="2"/><circle cx="178" cy="1030" r="2"/><circle cx="183" cy="1005" r="2"/><circle cx="188" cy="1000" r="2"/><circle cx="192" cy="990" r="2"/><circle cx="196" cy="1015" r="2"/><circle cx="201" cy="1025" r="2"/><circle cx="208" cy="1000" r="2"/><circle cx="212" cy="985" r="2"/><circle cx="216" cy="1010" r="2"/><circle cx="220" cy="962" r="2"/><circle cx="225" cy="1020" r="2"/><circle cx="229" cy="995" r="2"/><circle cx="234" cy="1000" r="2"/><circle cx="238" cy="970" r="2"/><circle cx="243" cy="1055" r="2"/><circle cx="246" cy="1010" r="2"/><circle cx="250" cy="1015" r="2"/><circle cx="254" cy="985" r="2"/><circle cx="258" cy="1048" r="2"/><circle cx="261" cy="1000" r="2"/><circle cx="264" cy="930" r="2"/><circle cx="267" cy="1022" r="2"/><circle cx="270" cy="1010" r="2"/><circle cx="273" cy="965" r="2"/><circle cx="276" cy="985" r="2"/><circle cx="280" cy="960" r="2"/><circle cx="285" cy="945" r="2"/><circle cx="290" cy="935" r="2"/><circle cx="296" cy="958" r="2"/><circle cx="302" cy="975" r="2"/><circle cx="310" cy="945" r="2"/><circle cx="318" cy="960" r="2"/><circle cx="326" cy="972" r="2"/><circle cx="333" cy="950" r="2"/><circle cx="342" cy="968" r="2"/><circle cx="350" cy="952" r="2"/><circle cx="358" cy="962" r="2"/><circle cx="365" cy="925" r="2"/><circle cx="372" cy="955" r="2"/><circle cx="380" cy="940" r="2"/><circle cx="388" cy="928" r="2"/><circle cx="396" cy="945" r="2"/>
      </g>
      <g fill="#2f7fc1">
        <circle cx="197" cy="958" r="2"/><circle cx="205" cy="983" r="2"/><circle cx="213" cy="975" r="2"/><circle cx="221" cy="1000" r="2"/><circle cx="226" cy="992" r="2"/><circle cx="232" cy="967" r="2"/><circle cx="240" cy="988" r="2"/><circle cx="243" cy="953" r="2"/><circle cx="250" cy="980" r="2"/><circle cx="255" cy="958" r="2"/><circle cx="258" cy="965" r="2"/><circle cx="260" cy="1040" r="2"/><circle cx="262" cy="945" r="2"/><circle cx="267" cy="975" r="2"/><circle cx="270" cy="955" r="2"/><circle cx="274" cy="1000" r="2"/><circle cx="278" cy="940" r="2"/><circle cx="282" cy="970" r="2"/><circle cx="283" cy="1043" r="2"/><circle cx="286" cy="1030" r="2"/><circle cx="289" cy="950" r="2"/><circle cx="292" cy="985" r="2"/><circle cx="295" cy="935" r="2"/><circle cx="298" cy="1005" r="2"/><circle cx="301" cy="960" r="2"/><circle cx="304" cy="990" r="2"/><circle cx="306" cy="925" r="2"/><circle cx="309" cy="1010" r="2"/><circle cx="312" cy="948" r="2"/><circle cx="314" cy="980" r="2"/><circle cx="316" cy="1005" r="2"/><circle cx="318" cy="918" r="2"/><circle cx="321" cy="965" r="2"/><circle cx="325" cy="940" r="2"/><circle cx="330" cy="928" r="2"/><circle cx="335" cy="955" r="2"/><circle cx="340" cy="935" r="2"/><circle cx="350" cy="950" r="2"/><circle cx="358" cy="930" r="2"/><circle cx="365" cy="955" r="2"/><circle cx="375" cy="945" r="2"/><circle cx="385" cy="938" r="2"/>
      </g>
      <line x1="160" y1="978" x2="418" y2="933" stroke="#2f7fc1" stroke-width="2"/>
      <line x1="152" y1="988" x2="418" y2="941" stroke="#9a9a9a" stroke-width="2"/>
      <g font-size="12" fill="#444" text-anchor="middle">
        <text transform="translate(141 860) rotate(-90)">100</text><text transform="translate(141 913) rotate(-90)">75</text><text transform="translate(141 965) rotate(-90)">50</text><text transform="translate(141 1016) rotate(-90)">25</text><text transform="translate(141 1067) rotate(-90)">0</text>
        <text x="160" y="1090">.3</text><text x="199" y="1090">.4</text><text x="237" y="1090">.5</text><text x="276" y="1090">.6</text><text x="314" y="1090">.7</text><text x="353" y="1090">.8</text><text x="392" y="1090">.9</text>
      </g>
    </symbol>

    <symbol id="trade" viewBox="105 1170 315 255">
      <g stroke="#dcdcdc" stroke-dasharray="4 4">
        <line x1="132" y1="1180" x2="415" y2="1180"/><line x1="132" y1="1218" x2="415" y2="1218"/><line x1="132" y1="1255" x2="415" y2="1255"/><line x1="132" y1="1327" x2="415" y2="1327"/><line x1="132" y1="1362" x2="415" y2="1362"/><line x1="132" y1="1392" x2="415" y2="1392"/>
        <line x1="182" y1="1175" x2="182" y2="1400"/><line x1="229" y1="1175" x2="229" y2="1400"/><line x1="276" y1="1175" x2="276" y2="1400"/><line x1="326" y1="1175" x2="326" y2="1400"/><line x1="378" y1="1175" x2="378" y2="1400"/>
      </g>
      <line x1="132" y1="1175" x2="132" y2="1400" stroke="#999"/>
      <line x1="132" y1="1400" x2="415" y2="1400" stroke="#999"/>
      <line x1="132" y1="1290" x2="415" y2="1290" stroke="#888"/>
      <g fill="#bcbcbc">
        <rect x="148" y="1270" width="4" height="42"/><rect x="155" y="1275" width="4" height="25"/><rect x="162" y="1284" width="4" height="10"/><rect x="176" y="1278" width="4" height="30"/><rect x="183" y="1250" width="4" height="58"/><rect x="190" y="1268" width="4" height="20"/><rect x="197" y="1278" width="4" height="24"/><rect x="204" y="1280" width="4" height="14"/><rect x="211" y="1284" width="4" height="8"/><rect x="225" y="1284" width="4" height="8"/><rect x="239" y="1286" width="4" height="6"/><rect x="253" y="1284" width="4" height="10"/><rect x="267" y="1280" width="4" height="16"/><rect x="281" y="1285" width="4" height="8"/><rect x="295" y="1284" width="4" height="8"/><rect x="309" y="1282" width="4" height="12"/><rect x="323" y="1284" width="4" height="8"/><rect x="337" y="1272" width="4" height="24"/><rect x="344" y="1276" width="4" height="36"/><rect x="358" y="1280" width="4" height="18"/><rect x="372" y="1276" width="4" height="58"/>
      </g>
      <g fill="#2f7fc1">
        <rect x="144" y="1258" width="4" height="42"/><rect x="151" y="1270" width="4" height="35"/><rect x="158" y="1282" width="4" height="14"/><rect x="165" y="1286" width="4" height="10"/><rect x="172" y="1268" width="4" height="44"/><rect x="179" y="1230" width="4" height="78"/><rect x="186" y="1260" width="4" height="38"/><rect x="193" y="1270" width="4" height="40"/><rect x="200" y="1274" width="4" height="22"/><rect x="207" y="1282" width="4" height="14"/><rect x="214" y="1278" width="4" height="20"/><rect x="221" y="1286" width="4" height="6"/><rect x="228" y="1285" width="4" height="9"/><rect x="235" y="1286" width="4" height="8"/><rect x="242" y="1283" width="4" height="13"/><rect x="249" y="1282" width="4" height="14"/><rect x="256" y="1286" width="4" height="8"/><rect x="263" y="1276" width="4" height="24"/><rect x="270" y="1286" width="4" height="8"/><rect x="277" y="1284" width="4" height="12"/><rect x="284" y="1286" width="4" height="6"/><rect x="291" y="1284" width="4" height="12"/><rect x="298" y="1278" width="4" height="26"/><rect x="305" y="1284" width="4" height="10"/><rect x="312" y="1286" width="4" height="6"/><rect x="319" y="1280" width="4" height="18"/><rect x="326" y="1284" width="4" height="10"/><rect x="333" y="1266" width="4" height="54"/><rect x="340" y="1268" width="4" height="60"/><rect x="347" y="1276" width="4" height="24"/><rect x="354" y="1272" width="4" height="22"/><rect x="361" y="1282" width="4" height="14"/><rect x="368" y="1266" width="4" height="40"/><rect x="379" y="1276" width="4" height="76"/>
      </g>
      <g font-size="12" fill="#444" text-anchor="middle">
        <text transform="translate(119 1180) rotate(-90)">6</text><text transform="translate(119 1218) rotate(-90)">4</text><text transform="translate(119 1255) rotate(-90)">2</text><text transform="translate(119 1290) rotate(-90)">0</text><text transform="translate(119 1327) rotate(-90)">-2</text><text transform="translate(119 1362) rotate(-90)">-4</text><text transform="translate(119 1392) rotate(-90)">-6</text>
        <text x="138" y="1421">0</text><text x="182" y="1421">20</text><text x="229" y="1421">40</text><text x="276" y="1421">60</text><text x="326" y="1421">.80</text><text x="378" y="1421">100</text>
      </g>
    </symbol>
  </defs>
</svg>

<main class="board">
  <h1 class="abs sheet-title">Charts and Table</h1>

  <table class="abs data-table">
    <thead><tr><th class="col-src">Sources</th><th class="col-yr">Years</th><th>Respondents</th></tr></thead>
    <tbody>
      <tr><td>Sahel Opinion Monitor</td><td>1999 – 2015</td><td>162,626</td></tr>
      <tr><td>Hemisphere Pulse</td><td>2004 – 2014</td><td>195,957</td></tr>
      <tr><td>Levant Voice Study</td><td>2006 – 2014</td><td>28,047</td></tr>
      <tr><td>Pacific Rim Attitudes Survey</td><td>2005 – 2010</td><td>22,355</td></tr>
      <tr><td>Cross-National Ballot Study</td><td>1996 – 2002</td><td>51,619</td></tr>
      <tr><td>Continental Social Panel</td><td>2012 – 2013</td><td>44,405</td></tr>
      <tr><td>Andes Opinión Panel</td><td>1995 – 2013</td><td>167,964</td></tr>
      <tr><td>Eastern Reform Monitor</td><td>2004 – 2005</td><td>13,271</td></tr>
      <tr><td>Citizen Echo Series</td><td>2000 – 2007</td><td>234,985</td></tr>
      <tr><td>Global Beliefs Inventory</td><td>2011 – 2014</td><td>45,776</td></tr>
    </tbody>
  </table>

  <svg class="abs chart-hist" role="img" aria-label="Histogram with fitted distribution curve"><use href="#hist"/></svg>

  <div class="abs legend legend-main"><span class="male"><i></i>Male</span><span class="female"><i></i>Female</span></div>

  <svg class="abs chart-scatter-l" viewBox="95 850 325 245" role="img" aria-label="Scatter plot of age by score with fitted lines">
    <text transform="translate(114 965) rotate(-90)" font-size="12" fill="#555" text-anchor="middle" letter-spacing="1">AGE</text>
    <use href="#scatter" x="125" y="850" width="295" height="245"/>
  </svg>
  <svg class="abs chart-scatter-r" role="img" aria-label="Scatter plot with fitted lines"><use href="#scatter"/></svg>

  <div class="abs chart-title title-l">TRADE VOLUME</div>
  <div class="abs chart-title title-r">TRADE VOLUME</div>
  <svg class="abs chart-trade-l" role="img" aria-label="Trade volume effect bars"><use href="#trade"/></svg>
  <svg class="abs chart-trade-r" role="img" aria-label="Trade volume effect bars"><use href="#trade"/></svg>

  <section class="abs site" aria-label="KOVAL Polls article page">
    <div class="topbar"><span>My Account</span><nav><span>Home</span><span>About us</span><span>Blog</span><span>Contact us</span></nav></div>
    <header class="masthead">
      <div class="brand"><i></i>KOVAL Polls</div>
      <nav class="mainnav"><span>Research<br>Library ⌄</span><span>Source<br>Datasets ⌄</span><span>Research<br>Tools ⌄</span><span>Resources &amp;<br>Downloads ⌄</span></nav>
    </header>
    <div class="hero" role="img" aria-label="Faint city skyline backdrop"></div>
    <div class="hero-copy">
      <div class="kicker">Version 3 Release:</div>
      <h2>Kindred Opinion Views Among Lands Polls</h2>
      <p>The first version of KOVAL Polls focuses on a limited set of variables: social trust, satisfaction with democracy, support for democracy, perceived electoral integrity, age, gender, education, and income.</p>
      <span class="btn">Latest Release</span>
    </div>
    <div class="toc">
      <h3><b>☰</b> Table of Contents:</h3>
      <div class="toc-cols">
        <div>1. Introduction<br>2. Data Setup Instructions<br>3. Demographic Divides in Perceptions...<br>4. Variables<br>5. Sources and Years</div>
        <div>6. Demographic Divides in Perceptions...<br>7. Economic Indicators and Satisfaction...<br>8. References<br>9. Sources of Datasets</div>
      </div>
    </div>
    <div class="divider"></div>

    <h3 class="sec-h" style="top:197px">1. Introduction:</h3>
    <p class="copy" style="top:206px">This article looks at two open issues in research on electoral integrity. First, demographic measures have produced mixed results that remain unresolved. Second, current electoral integrity indices may speak for some demographic groups more than others.</p>
    <h3 class="sec-h" style="top:243px">2. Data Setup Instructions</h3>
    <p class="copy" style="top:252px">Most statistical packages can open and analyse these datasets, but you will need a scripting tool to update and run the scripts. Later we may move to a free platform, but for now the scripts assume one common package. It is therefore expected that you have this software installed and a basic working knowledge of it. The steps below will get you set up and running as fast as possible.</p>
    <div class="step" style="top:290px"><i></i>Step 1: Setup File Structure ⌃</div>
    <p class="copy" style="top:303px">You can place your KOVAL Polls folder anywhere on your drive, but the folders and subfolders within it must match those named in the scripts. Renaming folders may mean you need to edit the scripts later. To save time we have made an empty folder tree you can download here. Unzip this folder where you want to set up your KOVAL Polls directory.</p>
    <p class="copy" style="top:341px">Note: the KOVAL Polls directory could eventually need over six gigabytes of hard drive space.</p>
    <div class="step" style="top:361px"><i></i>Step 2: Download Source Datasets ⌄</div>
    <div class="step" style="top:374px"><i></i>Step 3: Define Main Folder ⌄</div>
    <div class="step" style="top:386px"><i></i>Step 4: Run the Scripts ⌄</div>
    <div class="step" style="top:399px"><i></i>Step 5: Adding Sources and Variables ⌄</div>

    <h3 class="sec-h" style="top:422px">3. Data and Methods</h3>
    <p class="copy" style="top:432px">Public opinion data for this study comes from 35 cross-national surveys produced by the 10 sources summarised in Table 1.</p>
    <table class="mini-table">
      <thead><tr><th>Sources</th><th>Years</th><th>Respondents</th></tr></thead>
      <tbody>
        <tr><td>Sahel Opinion Monitor</td><td>1999 – 2015</td><td>162,626</td></tr>
        <tr><td>Hemisphere Pulse</td><td>2004 – 2014</td><td>195,957</td></tr>
        <tr><td>Levant Voice Study</td><td>2006 – 2014</td><td>28,047</td></tr>
        <tr><td>Pacific Rim Attitudes Survey</td><td>2005 – 2010</td><td>22,355</td></tr>
        <tr><td>Cross-National Ballot Study</td><td>1996 – 2002</td><td>51,619</td></tr>
        <tr><td>Continental Social Panel</td><td>2012 – 2013</td><td>44,405</td></tr>
        <tr><td>Andes Opinión Panel</td><td>1995 – 2013</td><td>167,964</td></tr>
        <tr><td>Eastern Reform Monitor</td><td>2004 – 2005</td><td>13,271</td></tr>
        <tr><td>Citizen Echo Series</td><td>2000 – 2007</td><td>234,985</td></tr>
        <tr><td>Global Beliefs Inventory</td><td>2011 – 2014</td><td>45,776</td></tr>
      </tbody>
    </table>

    <h3 class="sec-h" style="top:580px">4. Variables</h3>
    <p class="copy" style="top:590px;left:40px">2.1 Dependent Variables<br>The dependent variable here is perceived electoral integrity, in two versions: one for respondent data and another for country-year data. <i>See Figure 1.</i></p>
    <svg class="mini-hist" role="img" aria-label="Figure 1 histogram"><use href="#hist"/></svg>

    <h3 class="sec-h" style="top:730px">5. Results</h3>
    <p class="copy" style="top:740px">Results appear first as scatter plots in Figure 2. Light grey points show perceived electoral integrity scores for all respondents. The blue and grey lines show fitted values for contrasting demographic groups. The fitted lines trace patterns in group attitudes across levels of socioeconomic development and economic openness. Overall, attitudes toward electoral integrity rise with both measures, though the rates at which groups become more positive differ a great deal.</p>
    <div class="legend mini-legend"><span class="male"><i></i>Male</span><span class="female"><i></i>Female</span></div>
    <svg class="mini-scatter-l" viewBox="95 850 325 245" role="img" aria-label="Scatter plot of age by score">
      <text transform="translate(114 965) rotate(-90)" font-size="12" fill="#555" text-anchor="middle">AGE</text>
      <use href="#scatter" x="125" y="850" width="295" height="245"/>
    </svg>
    <svg class="mini-scatter-r" role="img" aria-label="Scatter plot"><use href="#scatter"/></svg>

    <h3 class="sec-h" style="top:904px">5. Data Visualisation</h3>
    <p class="copy" style="top:914px">Figure 3 shows results that sum up ninety bivariate multilevel regressions for each economic indicator. The variables in these models were built by combining eleven centiles around a central point. Bars at each point along the horizontal axis mark a regression using that centile with five centiles above and below it. Taller bars mean a stronger link, upward bars show positive effects and downward bars negative ones. Charts omit the first and last five bars because those models rest on fewer centiles and are less reliable.</p>
    <div class="mini-ct" style="left:57px;top:978px">TRADE VOLUME</div>
    <div class="mini-ct" style="left:182px;top:978px">TRADE VOLUME</div>
    <svg class="mini-trade-l" role="img" aria-label="Trade volume effect bars"><use href="#trade"/></svg>
    <svg class="mini-trade-r" role="img" aria-label="Trade volume effect bars"><use href="#trade"/></svg>

    <footer class="footer"></footer>
    <div class="foot-brand">
      <div class="brand"><i></i>KOVAL Polls</div>
      <p>Open survey data merged from many nations, checked for quality and shared freely with researchers everywhere.</p>
      <div class="social"><i></i><i></i><i></i></div>
    </div>
    <div class="foot-col" style="left:123px"><h4>Quick links</h4>Home<br>About us<br>Blog<br>Contact us</div>
    <div class="foot-col" style="left:166px"><h4>Resources</h4>Research Library<br>Source Datasets<br>Research Tools<br>Resources &amp; downloads</div>
    <div class="foot-col" style="left:230px;line-height:6.4px"><h4>Contact us</h4>Harbour Lane (B214), Westfield,<br>Region QX4 222<br>Call: +00 481 2290<br>Fax: +00 481 2291<br>Email: info@kovalpolls.org</div>
    <div class="bottombar">© KOVAL Polls. All rights reserved.</div>
  </section>
</main>
</body>
</html>
```